Landing Page Design for Adult Dating Age Verification (18+)

The objective of this task is to design a visually appealing pre-landing page for the adult dating site "Pivolunda (site: https://pivolunda.example/)" with an age verification mechanism. The pre-landing page will feature two buttons that redirect visitors to the main offer. The design should also include a footer block that includes links to the terms of use, privacy policy, and contact us pages.

Design Requirements:
Develop an age verification section prominently displayed on the pre-landing page.
Design the section to include two buttons labeled "Yes" and "No" for visitors to confirm their age.
Ensure the section is visually appealing and clearly communicates the purpose of age verification.

Visual Appeal:
Create a visually appealing design that aligns with the branding and theme of the "Pivolunda" adult dating site.
Use suitable color schemes, typography, and graphics to enhance the overall visual appeal of the pre-landing page.

Layout and Navigation:
Design an engaging and intuitive layout that encourages visitors to interact with the page and proceed to the main offer.
Ensure clear and visible navigation elements that direct visitors to the main offer or provide additional information.

Responsive Design:
Develop a responsive design that provides a seamless user experience across various devices, including desktop and mobile.
Ensure the design elements and layout adapt well to different screen sizes and resolutions.

File Formats and Assets:
Deliver the final design in PSD, AI, or Sketch format, ensuring that the files are well-organized and layered.
Include any necessary images or assets used in the design, ensuring they are of high quality and optimized for web use.

```html
<!DOCTYPE html>
<html lang="en">
<head>
<meta charset="utf-8">
<title>Pivolunda – Age Verification and Landing</title>
<link rel="stylesheet" href="https://fonts.googleapis.com/css2?family=Playfair+Display:wght@700;800&family=Montserrat:wght@400;500;600&display=swap">
<style>
:root{
  --ink:#2a2733;
  --board:#232323;
  --board-text:#ffffff;
  --lilac:#d4b2d7;
  --lilac-soft:#e7d8ea;
  --lilac-deep:#c7a3cb;
  --button:#d6acdc;
  --cream:#f0ebe8;
  --card:#efe9e7;
  --white:#ffffff;
  --serif:"Playfair Display", Georgia, serif;
  --sans:"Montserrat", Arial, sans-serif;
}
*{box-sizing:border-box;margin:0;padding:0}
html,body{width:1200px;height:2859px;overflow:hidden}
body{position:relative;background:var(--cream);color:var(--ink);font-family:var(--sans)}
.abs{position:absolute}
.board-band{left:0;width:1200px;background:var(--board)}
.board-label{color:var(--board-text);font-family:var(--sans);font-weight:500;font-size:19px;letter-spacing:.5px}
.backdrop{left:0;width:1200px}
.backdrop--age{top:88px;height:664px;background:linear-gradient(180deg,#e8dbea 0%,#d6bcd9 45%,#c9aacd 100%)}
.backdrop--hero{top:919px;height:720px;background:linear-gradient(180deg,#e7d6ea 0%,#d2b0d5 55%,#c8a5cc 100%)}
.brand{display:flex;align-items:center;gap:10px;font-family:var(--serif);font-weight:700;font-size:25px;color:var(--ink)}
.brand-dot{width:30px;height:30px;border-radius:50%;background:var(--lilac-deep)}
.nav{display:flex;gap:28px;font-family:var(--serif);font-weight:700;font-size:14px;letter-spacing:.5px;color:var(--ink)}
.pill{background:rgba(240,234,232,.82);border-radius:160px}
.age-question{left:235px;width:728px;top:361px;text-align:center;font-family:var(--serif);font-weight:700;font-size:35px;letter-spacing:1px}
.btn{display:flex;align-items:center;justify-content:center;border-radius:40px;font-family:var(--serif);font-weight:700;font-size:15px;letter-spacing:1px;color:var(--white);background:var(--button)}
.btn--light{background:var(--white);color:var(--ink)}
.photo{border-radius:50%}
.waves{left:0;top:919px}
.hero-title{left:309px;width:582px;top:1178px;text-align:center;font-family:var(--serif);font-weight:700;font-size:29px;line-height:37px;letter-spacing:1px}
.hero-sub{left:309px;width:582px;top:1266px;text-align:center;font-size:14.5px}
.link-text{font-family:var(--serif);font-weight:700;font-size:15px;letter-spacing:1px}
.section-title{left:0;width:1200px;text-align:center;font-family:var(--serif);font-weight:700;font-size:31px;letter-spacing:.5px}
.caps-title{left:0;width:1200px;text-align:center;font-family:var(--serif);font-weight:700;font-size:20px;letter-spacing:2px}
.body-copy{left:395px;width:410px;top:1797px;text-align:center;font-size:14.5px;line-height:25.5px;color:#3a3840}
.step{width:240px;text-align:center}
.step-label{position:absolute;top:95px;left:0;width:240px;font-size:16px}
.footer-kicker{left:109px;top:2480px;font-family:var(--serif);font-weight:700;font-size:19px;color:var(--white);letter-spacing:.5px}
.footer-title{left:109px;top:2516px;font-family:var(--serif);font-weight:800;font-size:45px;line-height:50px;letter-spacing:1.5px;color:var(--ink)}
.footer-rule{left:109px;top:2680px;width:982px;height:1px;background:rgba(255,255,255,.85)}
.footer-link{top:2717px;font-family:var(--serif);font-weight:700;font-size:15px;color:var(--white);letter-spacing:.5px}
.footer-url{left:0;width:1200px;top:2826px;text-align:center;font-size:15px;color:rgba(255,255,255,.6);letter-spacing:.5px}
</style>
</head>
<body>

<!-- Presentation: age verification screen -->
<div class="abs board-band" style="top:0;height:88px"></div>
<div class="abs board-label" style="left:104px;top:35px">AGE VERIFICATION SCREEN</div>

<section>
  <div class="abs backdrop backdrop--age" role="img" aria-label="Soft lilac-tinted blurred photo of a couple"></div>
  <div class="abs brand" style="left:105px;top:118px"><span class="brand-dot"></span>Pivolunda</div>
  <nav class="abs nav" style="left:950px;top:127px"><span>SIGN IN</span><span>JOIN</span></nav>
  <div class="abs pill" style="left:235px;top:283px;width:728px;height:285px"></div>
  <h1 class="abs age-question">Are you 18 years or older?</h1>
  <div class="abs btn" style="left:375px;top:433px;width:214px;height:62px">YES</div>
  <div class="abs btn btn--light" style="left:606px;top:433px;width:214px;height:62px">NO</div>
</section>

<!-- Presentation: main page -->
<div class="abs board-band" style="top:752px;height:167px"></div>
<div class="abs board-label" style="left:109px;top:864px">MAIN PAGE</div>

<section>
  <div class="abs backdrop backdrop--hero" role="img" aria-label="Lilac-tinted photo of a couple embracing"></div>
  <svg class="abs waves" width="1200" height="1940" viewBox="0 0 1200 1940" aria-hidden="true">
    <defs>
      <linearGradient id="footerFill" x1="0" y1="0" x2="0" y2="1">
        <stop offset="0" stop-color="#d3b0d6"/>
        <stop offset="1" stop-color="#d7b5da"/>
      </linearGradient>
    </defs>
    <path fill="#f0ebe8" d="M0 613 C80 560 160 482 258 482 C320 482 370 505 430 560 C520 640 600 735 777 740 C940 745 1080 700 1200 624 V1940 H0 Z"/>
    <path fill="url(#footerFill)" d="M0 1495 C70 1460 140 1447 220 1447 C420 1447 540 1560 720 1650 C850 1715 960 1730 1055 1726 C1120 1724 1170 1716 1200 1711 V1940 H0 Z"/>
  </svg>

  <div class="abs brand" style="left:105px;top:951px"><span class="brand-dot"></span>Pivolunda</div>
  <nav class="abs nav" style="left:964px;top:961px"><span>SIGN IN</span><span>JOIN</span></nav>

  <div class="abs photo" role="img" aria-label="Portrait photo of a woman by a window" style="left:208px;top:1046px;width:194px;height:194px;background:linear-gradient(135deg,#f1ece8,#7a5a48)"></div>
  <div class="abs photo" role="img" aria-label="Small portrait photo of a woman in red lingerie" style="left:860px;top:1143px;width:82px;height:82px;background:linear-gradient(135deg,#7b4a3e,#2d1e1c)"></div>
  <div class="abs photo" role="img" aria-label="Photo of a woman in a red bodysuit" style="left:828px;top:1292px;width:194px;height:194px;background:linear-gradient(135deg,#b8956c,#7d4a32)"></div>

  <div class="abs pill" style="left:309px;top:1138px;width:582px;height:249px;background:var(--card);border-radius:125px"></div>
  <h2 class="abs hero-title">Meet Your Dream Partner<br>With Pivolunda</h2>
  <p class="abs hero-sub">We will find your dream girl especially for you</p>
  <div class="abs btn" style="left:421px;top:1310px;width:168px;height:48px;font-size:14px">JOIN NOW</div>
  <div class="abs link-text" style="left:651px;top:1325px">LEARN MORE</div>

  <div class="abs photo" role="img" aria-label="Photo of a blonde woman sitting by a bed" style="left:103px;top:1419px;width:310px;height:310px;background:linear-gradient(135deg,#b08a5c,#dcc9c0 55%,#9fa9b6)"></div>

  <h2 class="abs section-title" style="top:1746px">The Best place to find her</h2>
  <p class="abs body-copy">Forget about looking through thousands of profiles every day and leave the finding to us. We will find the partner especailly suited to you and send a matching one everyday so you can start chatting right away.</p>
  <div class="abs photo" role="img" aria-label="Photo of a woman in black lace" style="left:851px;top:1747px;width:240px;height:240px;background:linear-gradient(135deg,#5a2a26,#1d1a1c)"></div>

  <h3 class="abs caps-title" style="top:1996px">SEE HOW EASY IT IS</h3>

  <div class="abs step" style="left:185px;top:2045px">
    <svg width="240" height="90" viewBox="0 0 240 90" aria-hidden="true">
      <circle cx="110" cy="28" r="30" fill="var(--lilac)"/>
      <g fill="none" stroke="#1f1d24" stroke-width="2">
        <rect x="110" y="20" width="44" height="56"/>
        <rect x="117" y="28" width="7" height="7"/><line x1="129" y1="31" x2="147" y2="31"/>
        <rect x="117" y="42" width="7" height="7"/><line x1="129" y1="45" x2="143" y2="45"/>
        <rect x="117" y="56" width="7" height="7"/><line x1="129" y1="59" x2="139" y2="59"/>
        <path d="M166 42 L146 70 L142 78 L150 73 L170 46 Z"/>
      </g>
    </svg>
    <span class="step-label">1. Fill Out The Form</span>
  </div>

  <div class="abs step" style="left:480px;top:2045px">
    <svg width="240" height="90" viewBox="0 0 240 90" aria-hidden="true">
      <circle cx="145" cy="57" r="28" fill="var(--lilac)"/>
      <g fill="none" stroke="#1f1d24" stroke-width="2">
        <rect x="87" y="23" width="66" height="46"/>
        <path d="M87 23 L120 50 L153 23"/>
        <path d="M87 69 L110 48 M153 69 L130 48"/>
        <path d="M112 54 L118 82 L123 74 L131 80 L134 77 L127 70 L134 66 Z" fill="var(--cream)"/>
      </g>
    </svg>
    <span class="step-label">2. Confirm Your Email</span>
  </div>

  <div class="abs step" style="left:749px;top:2045px">
    <svg width="240" height="90" viewBox="0 0 240 90" aria-hidden="true">
      <circle cx="110" cy="28" r="30" fill="var(--lilac)"/>
      <g fill="none" stroke="#1f1d24" stroke-width="2">
        <path d="M94 24 H148 V58 H112 L102 67 V58 H94 Z" fill="var(--cream)"/>
        <line x1="102" y1="34" x2="140" y2="34"/><line x1="102" y1="42" x2="140" y2="42"/><line x1="102" y1="50" x2="128" y2="50"/>
        <path d="M148 40 C160 40 166 48 166 56 C166 64 161 69 155 71 L158 78 L148 72 C138 72 132 66 130 58"/>
      </g>
    </svg>
    <span class="step-label">3. Start Chatting</span>
  </div>

  <h3 class="abs caps-title" style="top:2283px">SHE’S WAITING FOR YOU</h3>
  <div class="abs btn" style="left:515px;top:2325px;width:169px;height:49px;font-size:14px">JOIN NOW</div>

  <footer>
    <div class="abs footer-kicker">PIVOLUNDA</div>
    <h2 class="abs footer-title">The best advisor<br>in the dating world</h2>
    <div class="abs footer-rule"></div>
    <a class="abs footer-link" style="left:109px">Contact</a>
    <a class="abs footer-link" style="left:548px">Terms of Use</a>
    <a class="abs footer-link" style="left:977px">Privacy Policy</a>
    <div class="abs footer-url">PIVOLUNDA.EXAMPLE</div>
  </footer>
</section>

</body>
</html>
```